An anniversary gift for my girlfriend

My girlfriend and I have been dating for almost 2 years. We met online and this has afforded us the really unique opportunity to have the first words we said to each other (the whole conversation, in fact) preserved. We're moving in together in a few months and she doesn't know that I saved the conversation. I've been waiting for this to turn it into something we can hang in our new place.

The only phrase I want to use is:
"Well if you dislike people's knees then I think we'll get along famously"

It's an Never Quite Dusk in Marlowe Bay reference for the curious.

I want the poster to use the words themselves as the art; I'm thinking typography. I'd like it to match her aesthetic, she likes to wear Tessa Brook and R. Vane. Colors shouldn't be anything too "girly". Somewhere I'd like to include the date June 1, 2015. It shouldn't be a major piece of the poster though, just a way to denote the date.

It should fit (and be fully visible in) a 16x20 (inches) frame

Thanks in advance for the work!

Industry/Entity Type

Dating

Font styles to use
Serif
Decorative
Script

Requirements
Must have
• Must use only the words: "Well if you dislike people's knees then I think we'll get along famously"
• I want this to be typography, so making the phrase the center of the poster and the art itself.

```html
<!DOCTYPE html>
<html lang="en">
<head>
<meta charset="utf-8">
<title>Well if you dislike people's knees — anniversary typography poster</title>
<link rel="stylesheet" href="https://fonts.googleapis.com/css2?family=Alfa+Slab+One&family=Roboto+Slab:wght@900&display=swap">
<style>
  :root {
    --backdrop: #efeeeb;
    --paper-light: #e6d6b2;
    --paper-mid: #d2b88a;
    --paper-edge: #a9834a;
    --leaf: #6e8f2c;
    --leaf-deep: #4f6e1f;
    --umber: #4a2312;
    --brick: #b3261a;
    --mustard: #c99a2c;
  }
  html, body {
    margin: 0;
    width: 900px;
    height: 1200px;
    overflow: hidden;
    background: var(--backdrop);
  }
  .stage { display: block; width: 900px; height: 1200px; }
  .display { font-family: "Alfa Slab One", "Roboto Slab", serif; }
  .slab { font-family: "Roboto Slab", "Alfa Slab One", serif; font-weight: 900; }
  .stop-paper-light { stop-color: var(--paper-light); }
  .stop-paper-mid { stop-color: var(--paper-mid); }
  .stop-paper-edge { stop-color: var(--paper-edge); }
  .ink-leaf { fill: var(--leaf); }
  .ink-leaf-deep { fill: var(--leaf-deep); }
  .ink-umber { fill: var(--umber); }
  .ink-brick { fill: var(--brick); }
  .ink-mustard { fill: var(--mustard); }
</style>
</head>
<body>
<svg class="stage" viewBox="0 0 900 1200" xmlns="http://www.w3.org/2000/svg">
  <defs>
    <radialGradient id="paper-tone" cx="50%" cy="40%" r="75%">
      <stop offset="0" class="stop-paper-light"/>
      <stop offset="0.6" class="stop-paper-mid"/>
      <stop offset="1" class="stop-paper-edge"/>
    </radialGradient>
  </defs>

  <g class="poster" transform="translate(74 30)">
    <rect class="poster-sheet" width="751" height="1140" fill="url(#paper-tone)"/>

    <g class="type-column" transform="translate(186 0)">
      <rect class="rule-top ink-leaf" x="0" y="124" width="392" height="10"/>

      <text class="line-well display ink-leaf" x="0" y="220" font-size="84" textLength="392" lengthAdjust="spacingAndGlyphs">Well if you</text>
      <rect class="rule-thin ink-umber" x="0" y="234" width="392" height="4"/>

      <text class="line-dis display ink-umber" x="0" y="410" font-size="225" textLength="392" lengthAdjust="spacingAndGlyphs">Dis</text>
      <rect class="rule-accent ink-brick" x="236" y="422" width="156" height="6"/>

      <text class="line-like display ink-brick" x="0" y="615" font-size="200" textLength="392" lengthAdjust="spacingAndGlyphs">like</text>

      <text class="line-people display ink-mustard" x="0" y="712" font-size="104" textLength="392" lengthAdjust="spacingAndGlyphs">people's</text>
      <rect class="rule-thin ink-leaf" x="0" y="744" width="392" height="4"/>

      <text class="line-knees display ink-leaf" x="0" y="838" font-size="112" textLength="392" lengthAdjust="spacingAndGlyphs">KNEES</text>

      <text class="line-then slab ink-leaf-deep" x="0" y="882" font-size="38" textLength="354" lengthAdjust="spacingAndGlyphs">then I think we'll</text>
      <text class="line-along slab ink-umber" x="0" y="944" font-size="68" textLength="357" lengthAdjust="spacingAndGlyphs">GET ALONG</text>
      <text class="line-famously slab ink-brick" x="0" y="1002" font-size="66" textLength="357" lengthAdjust="spacingAndGlyphs">FAMOUSLY</text>

      <text class="date-stamp slab ink-brick" transform="translate(370 851) rotate(90)" x="0" y="0" font-size="26" textLength="151" lengthAdjust="spacingAndGlyphs">JUNE 1, 2015</text>

      <rect class="rule-base ink-brick" x="0" y="1014" width="392" height="12"/>
    </g>
  </g>
</svg>
</body>
</html>
```